Fresh and Modern Real Estate Land Website

This Real Estate Agent sells only land.
The wordpress design will need to work well with responsive Avada theme.
Colors should complement the attached Home-Header.jpg, the Sonoran Desert, Southwest Region of Arizona and Tucson.
Home page layout to include
- Logo Attached: NewLogo.png
- Agent Photo: MaeDorn.jpg
- Contact Detials: use Phone
- Slogan: "I've Never Shown a House"
- Static header or Main image (see Attached Home-Header.jpg) - The dimensions of this shot may not be correct for your design. Please select from similar stock if needed and provide stock photo id.
- Intro/Welcome Text See Attached: Intro.txt
- Vertical or Horizontal display of "New" listings (include: Photo, Price, exerpt/intro) see: Properties.zip
- Tools of the trade. Home page will have a section called "Tools Of the Trade" These are items the agent uses in her work. This seciton will need to be 3 or More Images about 100 characters of text and Title. These will rotate through about 12 different tools. see: tools-of-the-trade.zip
Footer to include Contact Info/Recent Blog Posts/Testimonial
No Social Network icons
Main Menu:
Home
Properties
Testimonials
Services
About Mae
Blog
Contact
- Marck Script google/Times new Roman is logo. Designers Choice.

```html
<!DOCTYPE html>
<html lang="en">
<head>
<meta charset="utf-8">
<title>Mae Dorn – Tucson Land Lady</title>
<link href="https://fonts.googleapis.com/css2?family=Open+Sans:ital,wght@0,400;0,600;1,400&family=Gelasio:ital@0;1&display=swap" rel="stylesheet">
<style>
:root{
  --orange:#ef7b22;
  --blue:#16b1e1;
  --ink:#3d3d3d;
  --muted:#555;
  --nav:#4a4a4a;
  --nav-dark:#3a3a3a;
  --rule:#cfcfcf;
  --footer:#25292b;
  --footer-bar:#3d4143;
  --white:#fff;
}
*{margin:0;padding:0;box-sizing:border-box}
html,body{width:681px;height:1200px;overflow:hidden;background:var(--white)}
body{position:relative;font-family:"Open Sans",Arial,sans-serif;color:var(--ink)}
.abs{position:absolute}
.serif{font-family:"Gelasio",Georgia,serif}

/* header */
.brand{left:67px;top:13px}
.brand-name{font-size:18px;font-weight:600;color:var(--orange);line-height:1;white-space:nowrap}
.brand-tag{font-size:5.6px;font-weight:600;color:var(--orange);letter-spacing:.3px;margin-top:3px;white-space:nowrap}
.agent-photo{left:172px;top:5px;width:42px;height:45px;background:linear-gradient(#d9c1ad,#b85a4a)}
.phone{left:518px;top:18px;font-size:14px;color:var(--orange);display:flex;align-items:center;gap:5px}

/* nav */
.nav{left:0;top:50px;width:681px;height:24px;background:linear-gradient(var(--nav),var(--nav-dark))}
.nav ul{list-style:none;display:flex;position:absolute;left:68px;top:0;height:24px}
.nav li{font-size:7px;color:var(--white);padding:0 12px;line-height:24px;border-right:1px solid #2f2f2f;white-space:nowrap}
.nav li.active{background:var(--orange)}
.nav-mail{left:482px;top:50px;width:199px;height:24px;background:var(--blue);clip-path:polygon(0 0,100% 0,100% 100%,0 100%,8px 50%);color:var(--white);font-size:7.5px;line-height:24px;padding-left:20px;white-space:nowrap}

/* hero */
.hero{left:0;top:74px;width:681px;height:252px;background:linear-gradient(#1d5f8f 0%,#3a7fa6 35%,#7b6a4c 55%,#4f5a2f 80%,#3f4a24 100%)}
.hero-title{left:0;top:154px;width:681px;text-align:center;font-size:21px;color:var(--white)}
.hero-rule{left:110px;top:185px;width:460px;height:1px;background:rgba(255,255,255,.8)}
.hero-text{left:120px;top:191px;width:441px;text-align:center;font-size:8.6px;line-height:10.5px;color:var(--white)}
.cta{left:297px;top:227px;width:86px;height:23px;background:var(--orange);color:var(--white);font-size:10px;text-align:center;line-height:23px;border-radius:2px}
.arrow{top:176px}

/* sections */
.section-title{left:0;width:681px;text-align:center;font-size:16px;color:var(--ink)}
.rule{height:1px;background:var(--rule)}
.welcome-text{left:92px;top:393px;width:497px;text-align:center;font-size:8.6px;line-height:10.5px;color:var(--muted)}
.accent{height:3px;display:flex}
.accent span{display:block;height:3px;background:#555}
.accent span.o{background:var(--orange)}

.tool{width:115px}
.tool-photo{width:115px;height:87px}
.tool-name{margin-top:11px;font-size:10.5px;color:var(--ink)}
.tool-text{margin-top:3px;font-size:6px;line-height:7.2px;color:var(--muted)}

.block-title{font-size:10.5px;color:var(--ink)}
.testimonial-photo{width:52px;height:60px;background:linear-gradient(#8a8a7a,#c23a3a)}
.quote{width:166px;font-family:"Gelasio",Georgia,serif;font-style:italic;font-size:6.2px;line-height:8.2px;color:var(--muted)}
.company{font-size:6.6px;font-style:italic;color:var(--blue)}
.pill{height:9px;background:var(--orange);color:var(--white);font-size:5.8px;font-style:italic;text-align:center;line-height:8px;border-radius:1px;border:1px solid #c95f12;white-space:nowrap}

.news-photo{width:59px;height:43px;background:linear-gradient(#8fb5d6 0%,#7b8b66 45%,#6f7a53 100%);position:absolute}
.price{position:absolute;left:0;bottom:0;width:59px;height:12px;background:rgba(20,20,20,.85);color:var(--white);font-size:6.5px;text-align:center;line-height:12px}
.news-title{font-size:8.2px;color:var(--ink)}
.news-date{font-family:"Gelasio",Georgia,serif;font-style:italic;font-size:6.4px;color:var(--blue)}
.news-text{font-size:5.8px;line-height:7px;color:var(--muted);width:150px}
.news-meta{font-size:5.5px;font-style:italic;color:#444}
.news-meta em{color:var(--orange);margin-left:4px}

/* footer */
.footer{left:0;top:1010px;width:681px;height:158px;background:var(--footer)}
.footer-bar{left:0;top:1168px;width:681px;height:32px;background:var(--footer-bar);color:var(--white);font-size:6px;text-align:center;line-height:8px;padding-top:6px}
.foot-head{font-size:8.6px;color:var(--white)}
.quick-links{list-style:none;font-size:6.2px;line-height:10.2px;color:var(--white)}
.blog-photo{width:34px;height:26px;background:linear-gradient(#9fbfd8,#7e8c63)}
.blog-title{font-family:"Gelasio",Georgia,serif;font-style:italic;font-size:6.4px;color:var(--white)}
.blog-text{font-size:6px;line-height:8px;color:var(--white);width:120px}
.map{left:355px;top:1043px;width:143px;height:71px;background:linear-gradient(135deg,#efe9d8,#dfe6ee)}
.foot-phone{left:509px;top:1040px;font-size:13px;color:var(--orange)}
.foot-mail{left:512px;top:1056px;font-size:8.6px;color:var(--white)}
</style>
</head>
<body>

<header>
  <div class="abs brand">
    <div class="brand-name">Mae Dorn</div>
    <div class="brand-tag">TUCSON'S #1 LAND LADY</div>
  </div>
  <div class="abs agent-photo" role="img" aria-label="Portrait of agent Mae Dorn"></div>
  <div class="abs phone">
    <svg width="7" height="11" viewBox="0 0 7 11"><rect x="0.6" y="0.6" width="5.8" height="9.8" rx="1" fill="none" stroke="#ef7b22" stroke-width="1.2"/><rect x="2.5" y="8.2" width="2" height="1" fill="#ef7b22"/></svg>
    <span>1800-555-214</span>
  </div>
</header>

<nav class="abs nav">
  <ul>
    <li>HOME</li>
    <li class="active">PROPERTIES</li>
    <li>TESTIMONIALS</li>
    <li>SERVICES</li>
    <li>ABOUT MAE</li>
    <li>BLOG</li>
    <li>CONTACT US</li>
  </ul>
</nav>
<div class="abs nav-mail">INFO@MAEDORNLANDLADY.COM</div>

<section>
  <div class="abs hero" role="img" aria-label="Sonoran desert mountains with saguaro cacti under a blue sky"></div>
  <svg class="abs arrow" style="left:66px" width="12" height="16" viewBox="0 0 12 16"><path d="M9 2 3 8l6 6" fill="none" stroke="rgba(255,255,255,.75)" stroke-width="2.2"/></svg>
  <svg class="abs arrow" style="left:600px" width="12" height="16" viewBox="0 0 12 16"><path d="M3 2l6 6-6 6" fill="none" stroke="rgba(255,255,255,.75)" stroke-width="2.2"/></svg>
  <h1 class="abs hero-title serif" style="font-weight:400">I've Never Shown a House</h1>
  <div class="abs hero-rule"></div>
  <p class="abs hero-text">Lorem ipsum dolor sit amet, consectetur adipisicing elit, sed do eiusmod tempor incididunt ut labore et dolore magna aliqua. Ut enim ad minim veniam, quis nostrud exercitation ullamco laboris nisi</p>
  <div class="abs cta">Call to Action</div>
</section>

<section>
  <h2 class="abs section-title serif" style="top:354px;font-weight:400">Welcome to the Land Lady</h2>
  <div class="abs rule" style="left:94px;top:384px;width:493px"></div>
  <p class="abs welcome-text">When you are looking for Tucson land, Mae Dorn's experience has "landed" her among the top 1/2% ranking of all Realtors, and that's just selling LAND!&nbsp; Mae is proud to say that she STILL has never sold a house... but she does know the best who do.&nbsp; 90% of real estate is sold by 10% of the Realtors and, during nearly 30 years of selling, Mae knows and is good friends with these 10%. Utilize Mae's contacts so she can match up the right home agent...for YOU!</p>
</section>

<section>
  <h2 class="abs section-title serif" style="top:462px;font-size:13.5px;font-weight:400">Tools of the Trade</h2>
  <div class="abs rule" style="left:94px;top:487px;width:493px"></div>
  <div class="abs accent" style="left:289px;top:484px"><span style="width:43px"></span><span class="o" style="width:16px"></span><span style="width:44px"></span></div>

  <article class="abs tool" style="left:94px;top:514px">
    <div class="tool-photo" role="img" aria-label="Desert scrubland with mountains in the distance" style="background:linear-gradient(#a9c7e0 0%,#8a9a7a 40%,#c9c0a6 100%)"></div>
    <h3 class="tool-name" style="font-weight:400">Red-Mountain</h3>
    <p class="tool-text">Lorem ipsum dolor sit amet, elit, sed do eiusmod tempor incididunt labore et dolore magna aliqua. Ut enim ad minim veniam, quis nostrud exercit ation ullamco laboris nisi..</p>
  </article>
  <article class="abs tool" style="left:220px;top:514px">
    <div class="tool-photo" role="img" aria-label="Orange desert sunset over a dark horizon" style="background:linear-gradient(#c9701a 0%,#f2a51e 45%,#6a3208 80%,#1c0d04 100%)"></div>
    <h3 class="tool-name" style="font-weight:400">Ave-Shelly</h3>
    <p class="tool-text">Lorem ipsum dolor sit amet, elit, sed do eiusmod tempor incididunt labore et dolore magna aliqua. Ut enim ad minim veniam, quis nostrud exercit ation ullamco laboris nisi..</p>
  </article>
  <article class="abs tool" style="left:346px;top:514px">
    <div class="tool-photo" role="img" aria-label="Saguaro cacti on a desert lot" style="background:linear-gradient(#7fa9d3 0%,#8d9a7b 40%,#7a7a55 100%)"></div>
    <h3 class="tool-name" style="font-weight:400">Turtle</h3>
    <p class="tool-text">Lorem ipsum dolor sit amet, elit, sed do eiusmod tempor incididunt labore et dolore magna aliqua. Ut enim ad minim veniam, quis nostrud exercit ation ullamco laboris nisi..</p>
  </article>
  <article class="abs tool" style="left:472px;top:514px">
    <div class="tool-photo" role="img" aria-label="Desert scrubland with mountains in the distance" style="background:linear-gradient(#a9c7e0 0%,#8a9a7a 40%,#c9c0a6 100%)"></div>
    <h3 class="tool-name" style="font-weight:400">Red-Mountain</h3>
    <p class="tool-text">Lorem ipsum dolor sit amet, elit, sed do eiusmod tempor incididunt labore et dolore magna aliqua. Ut enim ad minim veniam, quis nostrud exercit ation ullamco laboris nisi..</p>
  </article>
</section>

<section>
  <h3 class="abs block-title" style="left:106px;top:716px;font-weight:400">Testimonials</h3>
  <div class="abs rule" style="left:106px;top:737px;width:219px"></div>
  <div class="abs accent" style="left:106px;top:735px"><span class="o" style="width:16px"></span><span style="width:42px"></span></div>

  <div class="abs testimonial-photo" style="left:106px;top:754px" role="img" aria-label="Client portrait"></div>
  <p class="abs quote" style="left:163px;top:752px">“ Lorem ipsum dolor sit amet, consectetur adipisicing elit, sed do eiusmod tempor incididunt ut labore et dolore magna aliqua. Ut enim ad minim veniam, quis nostrud exercitation ullamco laboris nisi ut aliquip ex ea commodo consequat. Duis aute irure dolor in reprehenderit in voluptate velit esse cillum dolore eu fugiat nulla pariatur. Excepteur sint occaecat cupidatat non proident ”</p>
  <div class="abs company" style="left:163px;top:825px">Lorem Real Estate company</div>

  <div class="abs testimonial-photo" style="left:106px;top:855px" role="img" aria-label="Client portrait"></div>
  <p class="abs quote" style="left:163px;top:853px">“ Lorem ipsum dolor sit amet, consectetur adipisicing elit, sed do eiusmod tempor incididunt ut labore et dolore magna aliqua. Ut enim ad minim veniam, quis nostrud exercitation ullamco laboris nisi ut aliquip ex ea commodo consequat. Duis aute irure dolor in reprehenderit in voluptate velit esse cillum dolore eu fugiat nulla pariatur. Excepteur sint occaecat cupidatat non proident ”</p>
  <div class="abs company" style="left:163px;top:926px">Lorem Real Estate company</div>

  <div class="abs pill" style="left:264px;top:955px;width:56px">All Testimonials</div>
</section>

<section>
  <h3 class="abs block-title" style="left:354px;top:716px;font-weight:400">Latest News</h3>
  <div class="abs rule" style="left:354px;top:737px;width:222px"></div>
  <div class="abs accent" style="left:354px;top:735px"><span class="o" style="width:17px"></span><span style="width:42px"></span></div>

  <div class="news-photo" style="left:355px;top:754px" role="img" aria-label="Desert land parcel"><div class="price">$599 / Pyds</div></div>
  <div class="abs news-title" style="left:425px;top:751px">Lorem Ipsum news 1</div>
  <div class="abs news-date" style="left:425px;top:764px">October 13, 2014</div>
  <p class="abs news-text" style="left:426px;top:774px">Lorem ipsum dolor sit amet, elit, sed do eiusmod tempor incididunt labore et dolore</p>
  <div class="abs news-meta" style="left:425px;top:793px">Expert By : MaeDorn, <em>Learn More</em></div>

  <div class="news-photo" style="left:355px;top:820px" role="img" aria-label="Desert land parcel"><div class="price">$599 / Pyds</div></div>
  <div class="abs news-title" style="left:425px;top:817px">Lorem Ipsum news 1</div>
  <div class="abs news-date" style="left:425px;top:830px">October 13, 2014</div>
  <p class="abs news-text" style="left:426px;top:840px">Lorem ipsum dolor sit amet, elit, sed do eiusmod tempor incididunt labore et dolore</p>
  <div class="abs news-meta" style="left:425px;top:859px">Expert By : MaeDorn, <em>Learn More</em></div>

  <div class="news-photo" style="left:355px;top:887px" role="img" aria-label="Desert land parcel"><div class="price">$599 / Pyds</div></div>
  <div class="abs news-title" style="left:425px;top:884px">Lorem Ipsum news 1</div>
  <div class="abs news-date" style="left:425px;top:897px">October 13, 2014</div>
  <p class="abs news-text" style="left:426px;top:907px">Lorem ipsum dolor sit amet, elit, sed do eiusmod tempor incididunt labore et dolore</p>
  <div class="abs news-meta" style="left:425px;top:926px">Expert By : MaeDorn, <em>Learn More</em></div>

  <div class="abs pill" style="left:524px;top:955px;width:34px">All News</div>
</section>

<footer>
  <div class="abs footer"></div>
  <div class="abs foot-head" style="left:67px;top:1044px">Quick Links</div>
  <ul class="abs quick-links" style="left:68px;top:1062px">
    <li>Home</li><li>Properties</li><li>Testimonials</li><li>Services</li><li>About Mae</li><li>Blog</li><li>Contact</li>
  </ul>

  <div class="abs foot-head" style="left:142px;top:1044px">Recent Blog</div>
  <div class="abs blog-photo" style="left:143px;top:1062px" role="img" aria-label="Desert landscape"></div>
  <div class="abs blog-title" style="left:185px;top:1061px">Lorem Blog Title</div>
  <p class="abs blog-text" style="left:185px;top:1071px">Lorem ipsum dolor sit amet, elit, sed do eiusmod tempor incididunt labore</p>
  <div class="abs news-date" style="left:185px;top:1091px">October 13, 2014</div>

  <div class="abs blog-photo" style="left:143px;top:1111px" role="img" aria-label="Desert landscape"></div>
  <div class="abs blog-title" style="left:185px;top:1110px">Lorem Blog Title</div>
  <p class="abs blog-text" style="left:185px;top:1120px">Lorem ipsum dolor sit amet, elit, sed do eiusmod tempor incididunt labore</p>
  <div class="abs news-date" style="left:185px;top:1140px">October 13, 2014</div>

  <div class="abs map" role="img" aria-label="Road map showing the office location"></div>
  <div class="abs pill" style="left:402px;top:1125px;width:50px">Click to enlarge</div>

  <div class="abs foot-phone">1800-555-214</div>
  <div class="abs foot-mail">info@maedornlandlady.com</div>

  <div class="abs footer-bar">Copyright 2014 - www.maedornlandlady.com<br>All rights reserved / Terms of Policy</div>
</footer>

</body>
</html>
```